Redesign our Product Box!

We have a product box for our pet supplement we are looking to redesign. Please use the photoshop file of the current design for the logo/info/dieline and the concept picture of a bag we would like to see included in the box design.

Ideally the background will be the green with white text, but we really want it to be fun and appealing to pet owners so do not be scared to show your vision.

```html
<!DOCTYPE html>
<html lang="en">
<head>
<meta charset="utf-8">
<title>SeaMeadow Phytoplankton Powder – Box Dieline</title>
<link rel="stylesheet" href="https://fonts.googleapis.com/css2?family=Nunito:wght@400;700;900&family=Nunito+Sans:wght@400;600;700&family=Archivo+Narrow:wght@700&display=swap">
<style>
  :root {
    --green: #1fa64a;
    --green-dark: #1b6b34;
    --orange: #f0562b;
    --band-blue: #1e86d6;
    --sky: #0aa6e8;
    --cut: #e0262e;
    --white: #ffffff;
    --ink: #222222;
    --photo-warm: #a8672e;
    --photo-cool: #8a8f8c;
  }
  html, body { margin: 0; padding: 0; overflow: hidden; }
  body {
    width: 681px; height: 1200px; background: var(--white);
    display: flex; align-items: center; justify-content: center;
  }
  .dieline { display: block; width: 681px; height: 715px; }
  .cut { fill: var(--white); stroke: var(--cut); stroke-width: 1.4; }
  .panel { fill: var(--green); }
  .base-band { fill: var(--orange); }
  .body-copy { font-family: "Nunito Sans", sans-serif; font-size: 11.5px; fill: var(--white); }
  .brand { font-family: "Nunito", sans-serif; font-weight: 900; fill: var(--white); }
  .brand--front { fill: var(--green); }
  .print-side { font-family: "Nunito Sans", sans-serif; font-size: 36px; fill: #1a1a1a; }
  .facts-title { font-family: "Archivo Narrow", sans-serif; font-weight: 700; font-size: 21px; fill: var(--ink); }
  .facts-row { font-family: "Nunito Sans", sans-serif; font-size: 7.5px; fill: var(--ink); }
  .facts-fine { font-family: "Nunito Sans", sans-serif; font-size: 5px; fill: #555; }
  .warning { font-family: "Nunito Sans", sans-serif; font-size: 8.6px; fill: var(--white); }
  .distributor { font-family: "Nunito Sans", sans-serif; font-size: 11.5px; fill: var(--white); }
  .pure-band-text { font-family: "Nunito Sans", sans-serif; font-size: 14px; fill: var(--white); }
  .product-name { font-family: "Nunito", sans-serif; font-weight: 900; font-size: 24px; fill: var(--green-dark); }
  .audience { font-family: "Nunito Sans", sans-serif; font-size: 14.5px; fill: var(--sky); }
  .benefit { font-family: "Nunito Sans", sans-serif; font-size: 16px; fill: var(--white); }
  .callout { font-family: "Nunito", sans-serif; font-weight: 900; font-size: 12.5px; fill: var(--white); }
  .lot { font-family: "Nunito Sans", sans-serif; font-size: 14px; fill: var(--cut); }
</style>
</head>
<body>
<svg class="dieline" viewBox="0 0 1200 1260" xmlns="http://www.w3.org/2000/svg">
  <!-- tuck flaps and dust flaps -->
  <path class="cut" d="M133 207 C133 150 170 124 200 124 L368 124 C398 124 410 160 410 207 Z"/>
  <path class="cut" d="M60 440 L130 435 L130 942 L60 937 Z"/>
  <path class="cut" d="M412 280 L610 280 L612 408 L636 435 L412 435 Z"/>
  <path class="cut" d="M945 280 L1140 280 L1140 435 L918 435 L936 410 L945 400 Z"/>
  <path class="cut" d="M415 942 L636 942 L636 1097 L437 1097 L430 970 Z"/>
  <path class="cut" d="M918 942 L1140 942 L1140 960 L1125 975 L1115 1097 L918 1097 Z"/>
  <path class="cut" d="M636 942 L918 942 L918 1160 L910 1168 L915 1168 C915 1215 890 1252 870 1252 L685 1252 C660 1252 640 1215 640 1168 L636 1160 Z"/>
  <line x1="665" y1="1165" x2="890" y2="1165" stroke="#4a5fa8" stroke-width="1.5"/>
  <text class="print-side" x="730" y="322">PRINT</text>
  <text class="print-side" x="730" y="368">SIDE</text>
  <text class="lot" x="783" y="1062" text-anchor="middle">Exp: 22025/03/Lot No.:12222</text>

  <!-- top lid -->
  <rect class="panel" x="130" y="207" width="282" height="228"/>
  <text class="brand" x="271" y="323" font-size="22" text-anchor="middle" transform="rotate(180 271 323)">SeaMeadow</text>

  <!-- main body panels -->
  <rect class="panel" x="130" y="435" width="1010" height="478"/>
  <rect class="base-band" x="130" y="913" width="1010" height="29"/>
  <g stroke="#158a3b" stroke-width="1">
    <line x1="412" y1="435" x2="412" y2="942"/>
    <line x1="636" y1="435" x2="636" y2="942"/>
    <line x1="918" y1="435" x2="918" y2="942"/>
  </g>

  <!-- back panel: supplement facts -->
  <g class="supplement-facts">
    <rect x="158" y="467" width="225" height="175" fill="var(--white)"/>
    <rect x="161" y="471" width="216" height="115" fill="none" stroke="var(--ink)" stroke-width="1.2"/>
    <text class="facts-title" x="265" y="495" text-anchor="middle">Supplement Facts</text>
    <line x1="161" y1="502" x2="377" y2="502" stroke="var(--ink)" stroke-width="2"/>
    <text class="facts-row" x="174" y="514">Serving Size: 1 Scoop/Day</text>
    <text class="facts-row" x="174" y="523">Servings per Container: 30</text>
    <text class="facts-row" x="280" y="523">Amount per Serving</text>
    <text class="facts-row" x="352" y="523">%DV</text>
    <line x1="161" y1="530" x2="377" y2="530" stroke="var(--ink)" stroke-width="2"/>
    <text class="facts-row" x="174" y="548">Microalgae Nannochloropsis Gaditana</text>
    <text class="facts-row" x="324" y="548">500mg</text>
    <text class="facts-row" x="360" y="548">‡</text>
    <line x1="161" y1="563" x2="377" y2="563" stroke="var(--ink)" stroke-width="2"/>
    <text class="facts-row" x="174" y="577">‡ Daily value not established.</text>
    <text class="facts-fine" x="161" y="596">These statements have not been evaluated by the Food and Drug Administration.</text>
    <text class="facts-fine" x="161" y="604">This product is not intended to diagnose, treat, cure, or prevent any disease.</text>
    <text class="facts-fine" x="161" y="620">Store in a cool, dry place.</text>
  </g>
  <rect x="157" y="685" width="226" height="86" fill="none" stroke="var(--white)" stroke-width="1.5"/>
  <text class="warning" text-anchor="middle">
    <tspan x="270" y="702"><tspan font-weight="700">WARNINGS:</tspan> Check with a qualified healthcare</tspan>
    <tspan x="270" y="713">professional before using this product if you are</tspan>
    <tspan x="270" y="724">pregnant, breastfeeding, or taking blood thinners. You</tspan>
    <tspan x="270" y="735">should call your doctor for medical advice about serious</tspan>
    <tspan x="270" y="746">adverse events. To report a serious adverse event or</tspan>
    <tspan x="270" y="757">obtain product information contact: 1 800 555 0199</tspan>
  </text>
  <text class="distributor">
    <tspan x="160" y="822" font-style="italic">Distributed By:</tspan>
    <tspan x="160" y="837" font-weight="700">Seabright Nutrition Inc.</tspan>
    <tspan x="160" y="852">42 Harbour Road,</tspan>
    <tspan x="160" y="867">Halifax, Nova Scotia Canada</tspan>
    <tspan x="160" y="882">B3H 0A1</tspan>
  </text>

  <!-- side panel: story -->
  <text class="body-copy" text-anchor="middle">
    <tspan x="524" y="488">Our premium phytoplankton</tspan>
    <tspan x="524" y="503">powder is a extraordinary</tspan>
    <tspan x="524" y="518">supplement.  It infuses your</tspan>
    <tspan x="524" y="533">pet's body with pure,</tspan>
    <tspan x="524" y="548">plant-based nutrients and</tspan>
    <tspan x="524" y="563">potent antioxidants.</tspan>
    <tspan x="524" y="593">Phytoplankton goes beyond</tspan>
    <tspan x="524" y="608">ordinary supplements; it's a</tspan>
    <tspan x="524" y="623">path to optimal health. In just a</tspan>
    <tspan x="524" y="638">few weeks, your pet will</tspan>
    <tspan x="524" y="653">experience a feeling of calm and</tspan>
    <tspan x="524" y="668">strength, the kind of wellness</tspan>
    <tspan x="524" y="683">our customers often say they've</tspan>
    <tspan x="524" y="698">been seeking.</tspan>
    <tspan x="524" y="728">Join those who have discovered</tspan>
    <tspan x="524" y="743">the transformative power of</tspan>
    <tspan x="524" y="758">phytoplankton. See the</tspan>
    <tspan x="524" y="773">difference for yourself and</tspan>
    <tspan x="524" y="788">understand why it's not just a</tspan>
    <tspan x="524" y="803">supplement, but a revolution in</tspan>
    <tspan x="524" y="818">pet health and vitality.</tspan>
  </text>
  <text class="brand" x="524" y="888" font-size="19" text-anchor="middle">SeaMeadow</text>

  <!-- front panel -->
  <path d="M657 435 L899 435 L899 617 L778 642 L657 617 Z" fill="var(--white)"/>
  <path d="M661 435 L895 435 L895 614 L778 638 L661 614 Z" fill="none" stroke="var(--green)" stroke-width="1.5"/>
  <text class="brand brand--front" x="781" y="479" font-size="21" text-anchor="middle">SeaMeadow</text>
  <rect x="661" y="507" width="234" height="19" fill="var(--band-blue)"/>
  <text class="pure-band-text" x="777" y="522" text-anchor="middle">100% PURE MARINE</text>
  <text class="product-name" x="780" y="561" text-anchor="middle">PHYTOPLANKTON</text>
  <text class="product-name" x="780" y="588" text-anchor="middle">POWDER</text>
  <text class="audience" x="778" y="611" text-anchor="middle">FOR DOGS &amp; CATS</text>
  <defs>
    <linearGradient id="petPhotoTone" x1="0" y1="0" x2="1" y2="0">
      <stop offset="0" stop-color="var(--photo-warm)"/>
      <stop offset="0.7" stop-color="var(--photo-warm)"/>
      <stop offset="1" stop-color="var(--photo-cool)"/>
    </linearGradient>
  </defs>
  <rect x="676" y="646" width="192" height="228" rx="40" fill="url(#petPhotoTone)" opacity="0.85" role="img" aria-label="Photo of a golden retriever sitting beside a tabby cat"/>
  <rect x="682" y="883" width="193" height="60" fill="var(--sky)"/>
  <text class="benefit" text-anchor="middle">
    <tspan x="778" y="908">Foundational Nutrition</tspan>
    <tspan x="778" y="928">&amp; Super-Antioxidant</tspan>
  </text>

  <!-- side panel: directions -->
  <text class="body-copy" font-size="10.5">
    <tspan x="940" y="485">Directions:</tspan>
    <tspan x="940" y="498">For dogs &amp; cats</tspan>
    <tspan x="940" y="511">1/16tsp once per day.</tspan>
    <tspan x="940" y="524">Administer orally.</tspan>
    <tspan x="940" y="537">To be mixed into food.</tspan>
    <tspan x="940" y="550">1/16tsp = 1/2 the  included scoop.</tspan>
  </text>
  <line x1="989" y1="581" x2="1069" y2="581" stroke="var(--white)" stroke-width="1.2"/>
  <rect x="941" y="602" width="176" height="51" fill="var(--sky)"/>
  <text class="callout" text-anchor="middle">
    <tspan x="1029" y="624">UNLOCK NATURE'S</tspan>
    <tspan x="1029" y="639">NUTRIENT TREASURE:</tspan>
  </text>
  <text class="body-copy" font-size="10.5" text-anchor="middle">
    <tspan x="1029" y="680">Phytoplankton is the foundation of life,</tspan>
    <tspan x="1029" y="693">It is the first plant in the entire</tspan>
    <tspan x="1029" y="706">food chain.</tspan>
    <tspan x="1029" y="733">Phytoplankton is a microscopic</tspan>
    <tspan x="1029" y="746">powerhouse. Your pet's body absorbs</tspan>
    <tspan x="1029" y="759">billions of phytoplankton with every</tspan>
    <tspan x="1029" y="772">serving.</tspan>
    <tspan x="1029" y="798">Packed with the building blocks of life,</tspan>
    <tspan x="1029" y="811">phytoplankton addresses multiple</tspan>
    <tspan x="1029" y="824">aspects of your pet's health in one</tspan>
    <tspan x="1029" y="837">simple supplement.</tspan>
  </text>
  <text class="brand" x="1029" y="888" font-size="19" text-anchor="middle">SeaMeadow</text>

  <!-- outer cut line of body -->
  <rect x="130" y="435" width="1010" height="507" fill="none" stroke="var(--cut)" stroke-width="1.4"/>
</svg>
</body>
</html>
```